Luxury Skin care box that is screaming "I want what's inside"

My brand name is MIRAVELLE which is high-end organic and natural skin care. Being all natural, I am looking for a packaging box design that would visually imply that it's natural and organic. As well as being sophisticated and eye catching. I am seeing it being in sky blue/turquoise as well as leafy green and silver foil. And I am thinking of using embossing on it too for ornate elements perhaps. I am not strictly limited to those ideas and open to new ideas and vision. The word MIRA means 'youth' in multiple languages so the packaging should look like something youthful yet classy. Target demographics women 35-55.
Please note, that this is just 1 box for starters, but I have about 5-6 different sizes where the same design would need to be transferred also, as a next job. So it's a multiple step gig. And after that labels too.

I am attaching the logo and images of some color schemes and pictures that 'talk' to me.
I like the images of molecules as on pictures 7 and 8 having little green leaves in them. Would be nice to have it as an accent at the top of the box.
Generally the logo will be positioned in the bottom part of the box on a darker color . It will be in silver foil. Then gradually the color would go lighter to the top of the box where accents of the molecules would be.

Please keep in mind that my packaging bottle that would go into these boxes are of green color similar to the image 482915730264518837-KX-Tintora-Shade-of-the-Season.webp so the box has to have some accents of this color, like molecules and leaves in them. So they still will go together nicely.

Thank you

Target Market(s)

women 35-55

Industry/Entity Type

high end beauty

Font styles to use
Sans Serif

Requirements
Must have
• foil ornate areas, like leaves or molecule looking objects
Nice to have
• tintora color 56a300. This is the color we use currently so we need to stick to it to some degree.
Should not have
• look masculine

```html
<!DOCTYPE html>
<html lang="en">
<head>
<meta charset="utf-8">
<title>MIRAVELLE Natural Skincare Face Serum – Carton Dieline</title>
<link href="https://fonts.googleapis.com/css2?family=Cabin:wght@400;500&display=swap" rel="stylesheet">
<style>
  :root {
    --paper: #ffffff;
    --teal: #00b7c7;
    --teal-ink: #0aa3b6;
    --teal-deep: #0e9aab;
    --silver: #b9b9b9;
    --silver-light: #f2f2f4;
    --silver-dark: #8e8e8e;
    --cut: #4a4a4a;
    --fold: #f08a8a;
    --leaf: #3c9a3a;
    --sky: #8fd3ea;
  }
  html, body {
    margin: 0;
    padding: 0;
    width: 1200px;
    height: 1200px;
    overflow: hidden;
    background: var(--paper);
  }
  .dieline {
    display: block;
    width: 1200px;
    height: 1200px;
    font-family: "Cabin", sans-serif;
  }
  .cut { fill: none; stroke: var(--cut); stroke-width: 1.2; }
  .fold { fill: none; stroke: var(--fold); stroke-width: 1.4; stroke-dasharray: 14 5 2 5; }
  .panel-white { fill: var(--paper); }
  .panel-teal { fill: var(--teal); }
  .panel-body { fill: url(#bodyFade); }
  .foil-band { fill: url(#foilBand); }
  .stop-white { stop-color: var(--paper); }
  .stop-teal { stop-color: var(--teal); }
  .stop-foil { stop-color: var(--silver); }
  .stop-foil-light { stop-color: var(--silver-light); }
  .stop-foil-dark { stop-color: var(--silver-dark); }
  .stop-sky { stop-color: var(--sky); }
  .stop-leaf { stop-color: var(--leaf); }

  .brand-name { font-weight: 500; letter-spacing: 1px; }
  .brand-name--lid { fill: var(--silver); font-size: 36px; }
  .brand-name--front { fill: var(--silver-light); font-size: 36px; }
  .brand-dot--lid { fill: none; stroke: var(--silver); stroke-width: 3; }
  .brand-dot--front { fill: none; stroke: var(--silver-light); stroke-width: 3; }

  .title { fill: var(--teal-ink); font-weight: 500; font-size: 60px; letter-spacing: 1px; }
  .subtitle { fill: var(--teal-ink); font-weight: 400; font-size: 34px; }
  .section-heading { fill: var(--teal-ink); font-size: 28px; }
  .copy { fill: var(--teal-ink); font-size: 14.5px; }
  .section-heading--faint { fill: var(--teal-deep); opacity: 0.55; }
  .copy--faint { fill: var(--teal-deep); opacity: 0.45; }
  .volume { fill: var(--paper); font-size: 14px; letter-spacing: 0.5px; }
</style>
</head>
<body>
<svg class="dieline" viewBox="0 0 1920 1920" xmlns="http://www.w3.org/2000/svg">
  <defs>
    <linearGradient id="bodyFade" x1="0" y1="557" x2="0" y2="1373" gradientUnits="userSpaceOnUse">
      <stop offset="0.13" class="stop-white"/>
      <stop offset="0.68" class="stop-teal"/>
    </linearGradient>
    <linearGradient id="foilBand" x1="168" y1="0" x2="1763" y2="0" gradientUnits="userSpaceOnUse">
      <stop offset="0" class="stop-foil"/>
      <stop offset="0.13" class="stop-foil-light"/>
      <stop offset="0.26" class="stop-foil-dark"/>
      <stop offset="0.45" class="stop-foil"/>
      <stop offset="0.54" class="stop-foil-dark"/>
      <stop offset="0.66" class="stop-foil-light"/>
      <stop offset="0.8" class="stop-foil-dark"/>
      <stop offset="0.92" class="stop-foil-light"/>
      <stop offset="1" class="stop-foil"/>
    </linearGradient>
    <radialGradient id="serumArt" cx="0.5" cy="0.5" r="0.5">
      <stop offset="0" class="stop-sky"/>
      <stop offset="0.55" class="stop-sky" stop-opacity="0.8"/>
      <stop offset="1" class="stop-teal" stop-opacity="0"/>
    </radialGradient>
  </defs>

  <!-- Top closure -->
  <g class="top-closure">
    <path class="panel-white cut" d="M538 187 C538 120 590 70 636 57 L802 57 C850 70 898 120 898 187 Z"/>
    <path class="panel-white cut" d="M533 557 L533 192 Q533 187 538 187 L576 187 Q581 187 581 192 L581 198 M857 198 L857 192 Q857 187 862 187 L899 187 Q904 192 904 197 L904 557"/>
    <rect class="panel-white" x="533.6" y="198" width="370" height="359"/>
    <line class="fold" x1="581" y1="192" x2="857" y2="192"/>
    <path class="panel-white cut" d="M533 308 L236 308 L192 505 L168 530 L168 557"/>
    <path class="panel-white cut" d="M904 308 L1200 308 L1245 505 L1269 530 L1269 557"/>
  </g>

  <!-- Lid brand mark -->
  <g class="lid-brand">
    <circle class="brand-dot--lid" cx="719" cy="352" r="30"/>
    <text class="brand-name brand-name--lid" x="719" y="451" text-anchor="middle">MIRAVELLE</text>
  </g>

  <!-- Body panels -->
  <path class="panel-body cut" d="M168 557 L1647 557 L1763 577 L1763 1353 L1647 1373 L168 1373 Z"/>

  <!-- Bottom closure -->
  <g class="bottom-closure">
    <path class="panel-teal cut" d="M168 1373 L168 1403 L192 1427 L236 1623 L533 1623 L533 1373 Z"/>
    <path class="panel-teal cut" d="M904 1373 L904 1623 L1200 1623 L1245 1427 L1269 1403 L1269 1373 Z"/>
    <path class="panel-teal cut" d="M533 1373 L533 1738 Q533 1743 538 1743 L576 1743 Q581 1743 581 1738 L857 1738 Q857 1743 862 1743 L899 1743 Q904 1743 904 1738 L904 1373 Z"/>
    <path class="panel-teal cut" d="M538 1743 C538 1810 590 1860 636 1873 L802 1873 C850 1860 898 1810 898 1743 Z"/>
    <line class="fold" x1="581" y1="1738" x2="857" y2="1738"/>
  </g>

  <!-- Foil band -->
  <rect class="foil-band" x="168" y="1280" width="425" height="23"/>
  <rect class="foil-band" x="843" y="1280" width="920" height="23"/>

  <!-- Fold lines -->
  <g class="fold-lines">
    <line class="fold" x1="175" y1="557" x2="1269" y2="557"/>
    <line class="fold" x1="175" y1="1373" x2="1269" y2="1373"/>
    <line class="fold" x1="533" y1="557" x2="533" y2="1373"/>
    <line class="fold" x1="904" y1="557" x2="904" y2="1373"/>
    <line class="fold" x1="1275" y1="557" x2="1275" y2="1373"/>
    <line class="fold" x1="1647" y1="557" x2="1647" y2="1373"/>
  </g>

  <!-- Left side panel -->
  <g class="side-panel side-panel--left">
    <text class="section-heading" x="341" y="679" text-anchor="middle">Instructions</text>
    <text class="copy" x="228" y="712">
      <tspan x="228">Lorem Ipsum is simply dummy text of</tspan>
      <tspan x="228" dy="20.4">the printing and typesetting industry.</tspan>
      <tspan x="228" dy="20.4">Lorem Ipsum has been the industry's</tspan>
      <tspan x="228" dy="20.4">standard dummy text ever since the</tspan>
      <tspan x="228" dy="20.4">1500s, when an unknown printer</tspan>
      <tspan x="228" dy="20.4">took a galley of type and scrambled it</tspan>
      <tspan x="228" dy="20.4">to make a type specimen book.</tspan>
    </text>
    <text class="section-heading" x="341" y="904" text-anchor="middle">Caution</text>
    <text class="copy" x="228" y="937">
      <tspan x="228">Lorem Ipsum is simply dummy text of</tspan>
      <tspan x="228" dy="20.4">the printing and typesetting industry.</tspan>
      <tspan x="228" dy="20.4">Lorem Ipsum has been the industry's</tspan>
      <tspan x="228" dy="20.4">standard dummy text ever since the</tspan>
      <tspan x="228" dy="20.4">1500s, when an unknown printer</tspan>
      <tspan x="228" dy="20.4">took a galley of type and scrambled it</tspan>
      <tspan x="228" dy="20.4">to make a type specimen book.</tspan>
    </text>
    <text class="section-heading section-heading--faint" x="341" y="1135" text-anchor="middle">Warning</text>
    <text class="copy copy--faint" x="228" y="1168">
      <tspan x="228">Lorem Ipsum is simply dummy text of</tspan>
      <tspan x="228" dy="20.4">the printing and typesetting industry.</tspan>
    </text>
  </g>

  <!-- Front panel -->
  <g class="front-panel">
    <text class="title" x="719" y="677" text-anchor="middle">NATURAL</text>
    <text class="title" x="719" y="735" text-anchor="middle">SKINCARE</text>
    <text class="subtitle" x="719" y="785" text-anchor="middle">FACE SERUM</text>
    <g role="img" aria-label="Illustration: translucent sky-blue serum sphere with clouds, ringed by turquoise dots and green leafy sprigs">
      <ellipse cx="718" cy="970" rx="165" ry="160" fill="url(#serumArt)"/>
    </g>
    <circle class="brand-dot--front" cx="719" cy="1205" r="30"/>
    <text class="brand-name brand-name--front" x="719" y="1303" text-anchor="middle">MIRAVELLE</text>
    <text class="volume" x="719" y="1343" text-anchor="middle">1.25 FL. OZ. (37 ML)</text>
  </g>

  <!-- Right side panel -->
  <g class="side-panel side-panel--right">
    <text class="section-heading" x="1087" y="679" text-anchor="middle">Lorem Ipsum</text>
    <text class="copy" x="970" y="712">
      <tspan x="970">Lorem Ipsum is simply dummy text of</tspan>
      <tspan x="970" dy="20.4">the printing and typesetting industry.</tspan>
      <tspan x="970" dy="20.4">Lorem Ipsum has been the industry's</tspan>
      <tspan x="970" dy="20.4">standard dummy text ever since the</tspan>
      <tspan x="970" dy="20.4">1500s, when an unknown printer took</tspan>
      <tspan x="970" dy="20.4">a galley of type and scrambled it to</tspan>
      <tspan x="970" dy="20.4">make a type specimen book. It has</tspan>
      <tspan x="970" dy="20.4">survived not only five centuries, but</tspan>
      <tspan x="970" dy="20.4">also the leap into electronic</tspan>
      <tspan x="970" dy="20.4">typesetting, remaining essentially</tspan>
      <tspan x="970" dy="20.4">unchanged. It was popularised in the</tspan>
      <tspan x="970" dy="20.4">1960s with the release of Lumatype</tspan>
      <tspan x="970" dy="20.4">sheets containing Lorem Ipsum</tspan>
      <tspan x="970" dy="20.4">passages, and more recently with</tspan>
      <tspan x="970" dy="20.4">desktop publishing software like Quillo</tspan>
      <tspan x="970" dy="20.4">Pagecraft including versions of Lorem</tspan>
      <tspan x="970" dy="20.4">Ipsum.</tspan>
    </text>
  </g>
</svg>
</body>
</html>
```